Brightvale Solutions company needs a homepage design

We need a homepage designed for a new company based in Des Moines, IA called Go Brightvale Solutions. They sell Carewell Supplement plans to seniors. The design should communicate trust, security, be vibrant and easy to read with larger font and clear messages. The goal for visitors is to ultimately get a free quote and purchase a plan after a call from a licensed agent.

```html
<!DOCTYPE html>
<html lang="en">
<head>
<meta charset="utf-8">
<title>Go Brightvale Solutions</title>
<link href="https://fonts.googleapis.com/css2?family=Open+Sans:wght@400;600;700&display=swap" rel="stylesheet">
<style>
:root{
  --navy:#0b4c9f;
  --navy-dark:#073a7d;
  --sky:#0aa6e8;
  --ink:#222;
  --muted:#777;
  --line:#ddd;
  --panel:#f2f2f2;
  --footer:#f5f5f5;
  --bottom:#e9e9e9;
  --white:#fff;
}
*{box-sizing:border-box;margin:0;padding:0}
html,body{width:1200px;height:2546px;overflow:hidden;background:var(--white);font-family:"Open Sans",sans-serif;color:var(--ink)}
.page{position:relative;width:1200px;height:2546px}
.abs{position:absolute}

/* header */
.site-header{left:0;top:0;width:1200px;height:92px}
.brand{left:132px;top:28px;display:flex;align-items:center;gap:12px;font-size:28px;font-weight:600;color:var(--navy);line-height:1}
.brand-mark{width:22px;height:22px;background:var(--sky);display:block}
.search{left:688px;top:31px;width:200px;height:27px;border:1px solid #ccc;background:#f7f7f7;font-size:11px;color:#777;padding:5px 9px;display:flex;justify-content:space-between;align-items:center}
.btn-sm{top:31px;height:27px;color:var(--white);font-size:11px;display:flex;align-items:center;justify-content:center;gap:5px}
.btn-login{left:903px;width:73px;background:var(--navy)}
.btn-register{left:988px;width:80px;background:var(--sky)}

.main-nav{left:0;top:92px;width:1200px;height:39px;background:var(--navy);display:flex;padding-left:132px}
.main-nav a{color:var(--white);font-size:11.5px;text-decoration:none;padding:0 18px;line-height:39px}
.main-nav a.active{background:var(--navy-dark)}

/* hero */
.hero{left:0;top:131px;width:1200px;height:482px;background:linear-gradient(100deg,#e9eef2 0%,#dfe5ea 30%,#eef1f3 55%,#d9dfe3 100%)}
.hero-card{left:400px;top:130px;width:400px;height:225px;background:rgba(255,255,255,.9);text-align:center;padding:22px 20px}
.hero-card h1{font-size:17px;font-weight:700;line-height:1.4;color:#222}
.hero-card p{font-size:10.5px;line-height:1.65;color:#333;margin-top:10px}
.btn-quote{display:inline-flex;align-items:center;gap:6px;margin-top:18px;background:var(--sky);color:var(--white);font-size:14px;font-weight:700;padding:10px 18px}
.hero-arrow{top:228px;width:28px;height:28px;background:rgba(120,120,120,.7);display:flex;align-items:center;justify-content:center}

/* partners */
.partners{left:0;top:613px;width:1200px;height:97px;background:var(--panel);display:flex;align-items:center;justify-content:space-between;padding:0 132px}
.partners span{font-size:18px;font-weight:600;color:#555}

/* welcome */
.welcome{left:132px;top:780px;width:936px;text-align:center}
.section-title{font-size:28px;font-weight:600;color:var(--navy);text-transform:uppercase;letter-spacing:.2px}
.welcome p{font-size:11px;line-height:1.85;color:#666;margin-top:10px}
.features{left:132px;top:933px;width:936px;display:flex;justify-content:space-between}
.feature{width:298px;height:208px;background:var(--sky);color:var(--white);text-align:center;padding-top:30px}
.feature h3{font-size:19px;font-weight:600;margin-top:12px}
.feature p{font-size:10.5px;line-height:1.7;margin:10px auto 0;width:220px}

/* plans */
.plans{left:0;top:1222px;width:1200px;height:480px;background:linear-gradient(180deg,#f1f3f5,#e8ecef)}
.plans .section-title{position:absolute;left:0;top:70px;width:1200px;text-align:center}
.tabs{position:absolute;left:132px;width:936px;display:flex;justify-content:center;gap:8px}
.tabs span{background:var(--navy);color:var(--white);font-size:12px;padding:0 13px;line-height:34px}
.tabs span.active{background:var(--sky)}
.tiles{position:absolute;left:132px;top:226px;width:936px;display:flex;justify-content:space-between}
.tile{width:219px}
.tile .ph{height:160px}
.tile p{font-size:12px;line-height:1.45;margin-top:8px;color:#222}

/* blog */
.blog{left:132px;top:1770px;width:936px}
.blog h2{text-align:center;font-size:29px;font-weight:400}
.pager{position:absolute;top:12px;width:22px;height:22px;border:1px solid #999;display:flex;align-items:center;justify-content:center}
.posts{display:flex;justify-content:space-between;margin-top:24px}
.post{width:298px}
.post .ph{height:192px}
.post time{display:block;font-size:12.5px;color:#555;margin-top:27px}
.post h4{font-size:13.5px;font-weight:400;line-height:1.5;margin-top:10px}
.post p{font-size:10.5px;line-height:1.75;color:#888;margin-top:10px}

/* footer */
.footer{left:0;top:2255px;width:1200px;height:218px;background:var(--footer)}
.col{position:absolute;top:28px}
.col h5{font-size:17px;font-weight:400;color:#222;margin-bottom:18px}
.col ul{list-style:none}
.col li{font-size:11px;color:#555;line-height:24px}
.col li::before{content:"›";margin-right:9px;color:#555}
.newsletter{position:absolute;left:826px;top:73px;width:242px;height:38px;border:1px solid #ccc;background:var(--white);font-size:11px;color:#888;display:flex;align-items:center;justify-content:space-between;padding:0 14px}
.follow{position:absolute;left:826px;top:125px;font-size:10.5px;color:#444}
.social{position:absolute;left:826px;top:149px;display:flex;gap:7px}
.social i{width:25px;height:25px;border-radius:50%;display:block}
.copyright{left:0;top:2473px;width:1200px;height:73px;background:var(--bottom);text-align:center;font-size:11px;color:#555;line-height:73px}
</style>
</head>
<body>
<div class="page">

<header class="site-header abs">
  <div class="brand abs"><i class="brand-mark"></i>Go Brightvale Solutions</div>
  <div class="search abs">Search
    <svg width="11" height="11" viewBox="0 0 12 12"><circle cx="5" cy="5" r="3.8" fill="none" stroke="#555" stroke-width="1.5"/><line x1="8" y1="8" x2="11" y2="11" stroke="#555" stroke-width="1.6"/></svg>
  </div>
  <div class="btn-sm btn-login abs">
    <svg width="10" height="10" viewBox="0 0 10 10"><path d="M1 5h6M5 2l3 3-3 3" stroke="#fff" stroke-width="1.5" fill="none"/></svg>Log in</div>
  <div class="btn-sm btn-register abs">
    <svg width="10" height="10" viewBox="0 0 10 10"><rect x="1" y="1" width="8" height="8" fill="none" stroke="#fff" stroke-width="1.3"/><path d="M3 7l4-4" stroke="#fff" stroke-width="1.3"/></svg>Register</div>
</header>

<nav class="main-nav abs">
  <a class="active">HOME</a><a>ABOUT US</a><a>PLANS</a><a>CATEGORY</a><a>BLOG</a><a>FAQS</a><a>CONTACT US</a>
</nav>

<section class="hero abs" role="img" aria-label="Photo of pill bottles and spilled capsules on a desk with a clipboard">
  <div class="hero-arrow abs" style="left:0"><svg width="12" height="12" viewBox="0 0 12 12"><path d="M10 6H2M5 3L2 6l3 3" stroke="#fff" stroke-width="1.6" fill="none"/></svg></div>
  <div class="hero-arrow abs" style="left:1172px"><svg width="12" height="12" viewBox="0 0 12 12"><path d="M2 6h8M7 3l3 3-3 3" stroke="#fff" stroke-width="1.6" fill="none"/></svg></div>
  <div class="hero-card abs">
    <h1>DUIS SCELERISQUE VEHICULA RISUS,<br>VITAE ORNARE LIGULA BLANDIT TEMPOR</h1>
    <p>Proin vitae eros non neque sodales vulputate. Sed ultricies diam in urna fringilla, eu ornare leo aliquet. Ut malesuada sapien est, in elementum felis commodo nec.</p>
    <span class="btn-quote"><svg width="12" height="12" viewBox="0 0 12 12"><rect x="1" y="2" width="9" height="9" fill="none" stroke="#fff" stroke-width="1.3"/><path d="M4 8l6-6" stroke="#fff" stroke-width="1.5"/></svg>GET A FREE QUOTE</span>
  </div>
</section>

<div class="partners abs">
  <span>Tidemark</span><span>Halvern</span><span>Kestrel</span><span>Oakridge</span><span>Lumina</span><span>Norvale</span><span>Sundial</span>
</div>

<section class="welcome abs">
  <h2 class="section-title">Welcome to Go Brightvale Solutions</h2>
  <p>Donec sit amet pulvinar arcu. Vivamus in elit posuere, commodo ante id, dapibus elit. Pellentesque a ante elementum, semper ante at, volutpat orci. Nullam ut justo hendrerit, eleifend ex sit amet, faucibus tortor. Nullam convallis, ipsum at dignissim blandit, justo sapien sagittis diam, sed scelerisque nulla mi eget massa. In aliquet arcu tempor nibh sagittis pulvinar eget at tellus. Pellentesque ullamcorper tempor mauris. Vivamus blandit iaculis lacus non lacinia. Vestibulum faucibus diam in consectetur volutpat. Fusce tristique ut dui non consequat. Aliquam a risus ac ante sagittis pellentesque id non mi.</p>
</section>

<div class="features abs">
  <div class="feature">
    <svg width="36" height="40" viewBox="0 0 36 40"><circle cx="18" cy="11" r="8" fill="#fff"/><path d="M3 39c0-10 7-15 15-15s15 5 15 15z" fill="#fff"/><path d="M12 26v6a3 3 0 0 0 6 0" stroke="#0aa6e8" stroke-width="2" fill="none"/><circle cx="24" cy="31" r="2.5" fill="#0aa6e8"/></svg>
    <h3>Created by Experts</h3>
    <p>Integer quam mi, pretium non vehicula pulvinar, elementum sit amet dui. Nulla ut tortor tristique, cursus ipsum in, rutrum nisl.</p>
  </div>
  <div class="feature">
    <svg width="36" height="40" viewBox="0 0 36 40"><path d="M4 2h18l8 8v20H4z" fill="none" stroke="#fff" stroke-width="2.4"/><path d="M9 14h14M9 20h14M9 26h8" stroke="#fff" stroke-width="2"/><circle cx="27" cy="31" r="8" fill="#fff"/><path d="M23 31l3 3 5-6" stroke="#0aa6e8" stroke-width="2.2" fill="none"/></svg>
    <h3>Best Plans</h3>
    <p>Integer quam mi, pretium non vehicula pulvinar, elementum sit amet dui. Nulla ut tortor tristique, cursus ipsum in, rutrum nisl.</p>
  </div>
  <div class="feature">
    <svg width="40" height="40" viewBox="0 0 40 40"><circle cx="13" cy="6" r="4.5" fill="#fff"/><circle cx="27" cy="6" r="4.5" fill="#fff"/><path d="M8 13h10v13h-2v13h-6V26H8z" fill="#fff"/><path d="M22 13h10l3 16h-5v10h-6V29h-4z" fill="#fff"/><path d="M5 17v22" stroke="#fff" stroke-width="2"/><path d="M37 17v22" stroke="#fff" stroke-width="2"/></svg>
    <h3>Categorized by Age</h3>
    <p>Integer quam mi, pretium non vehicula pulvinar, elementum sit amet dui. Nulla ut tortor tristique, cursus ipsum in, rutrum nisl.</p>
  </div>
</div>

<section class="plans abs">
  <h2 class="section-title">Carewell Supplement Plans</h2>
  <div class="tabs" style="top:123px">
    <span class="active">Arthritis</span><span>Heart Disease</span><span>Cancer</span><span>Respiratory Diseases</span><span>Alzheimer's Disease</span><span>Osteoporosis</span><span>Diabetes</span><span>Influenza and Pneumonia</span>
  </div>
  <div class="tabs" style="top:167px">
    <span>Falls</span><span>Substance Abuse</span><span>Obesity</span><span>Depression</span><span>Oral Health</span><span>Shingles</span><span>More</span>
  </div>
  <div class="tiles">
    <div class="tile"><div class="ph" role="img" aria-label="Photo of a senior choosing items at a pharmacy counter" style="background:linear-gradient(135deg,#e7e9ec,#9fb6d6)"></div><p>Praesent interdum auctor diam et finibus</p></div>
    <div class="tile"><div class="ph" role="img" aria-label="Photo of a stethoscope, pills and a small cart on a blue surface" style="background:linear-gradient(135deg,#2aa8d8,#7fd1ec)"></div><p>Praesent interdum auctor diam et finibus</p></div>
    <div class="tile"><div class="ph" role="img" aria-label="Close-up photo of green capsules" style="background:linear-gradient(135deg,#5cbf9e,#b9e3d2)"></div><p>Praesent interdum auctor diam et finibus</p></div>
    <div class="tile"><div class="ph" role="img" aria-label="Photo of pills in blister packs" style="background:linear-gradient(135deg,#c7d4cf,#8fa9a0)"></div><p>Praesent interdum auctor diam et finibus</p></div>
  </div>
</section>

<section class="blog abs">
  <h2>Blog</h2>
  <div class="pager" style="left:0"><svg width="8" height="8" viewBox="0 0 8 8"><path d="M6 1L2 4l4 3" stroke="#555" fill="none"/></svg></div>
  <div class="pager" style="left:914px"><svg width="8" height="8" viewBox="0 0 8 8"><path d="M2 1l4 3-4 3" stroke="#555" fill="none"/></svg></div>
  <div class="posts">
    <article class="post"><div class="ph" role="img" aria-label="Photo of a hand signing a form with a pen" style="background:linear-gradient(135deg,#f1f3f6,#c9d2dc)"></div><time>25 April, 2017</time><h4>Pellentesque dignissim nec quam vitae tinci dunt. Curabitur consectetur efficitur odio.</h4><p>Proin faucibus, elit ac ornare rutrum, urna risus pretium ante, in iaculis metus sapien ac nisl. Mauris vitae mauris tristique, sagittis libero eget, bibendum ante.</p></article>
    <article class="post"><div class="ph" role="img" aria-label="Photo of a person reading a medication leaflet" style="background:linear-gradient(135deg,#3e6d9c,#c9a98a)"></div><time>25 April, 2017</time><h4>Pellentesque dignissim nec quam vitae tinci dunt. Curabitur consectetur efficitur odio.</h4><p>Proin faucibus, elit ac ornare rutrum, urna risus pretium ante, in iaculis metus sapien ac nisl. Mauris vitae mauris tristique, sagittis libero eget, bibendum ante.</p></article>
    <article class="post"><div class="ph" role="img" aria-label="Photo of assorted medicine bottles and boxes" style="background:linear-gradient(135deg,#c8473f,#e8c36a)"></div><time>25 April, 2017</time><h4>Pellentesque dignissim nec quam vitae tinci dunt. Curabitur consectetur efficitur odio.</h4><p>Proin faucibus, elit ac ornare rutrum, urna risus pretium ante, in iaculis metus sapien ac nisl. Mauris vitae mauris tristique, sagittis libero eget, bibendum ante.</p></article>
  </div>
</section>

<footer class="footer abs">
  <div class="col" style="left:132px"><h5>Links</h5><ul><li>Home</li><li>About Us</li><li>Plans</li><li>Category</li><li>Blog</li></ul></div>
  <div class="col" style="left:230px;top:70px"><ul><li>FAQs</li><li>Contact Us</li></ul></div>
  <div class="col" style="left:411px"><h5>Support</h5><ul><li>Suspendisse</li><li>Morbi cursus</li><li>Fusce id</li><li>Pellentesque</li><li>Nulla faucibus</li></ul></div>
  <div class="col" style="left:611px"><h5>Donec blandit</h5><ul><li>Suspendisse</li><li>Morbi cursus</li><li>Fusce id</li><li>Pellentesque</li><li>Nulla faucibus</li></ul></div>
  <div class="col" style="left:826px"><h5>Newsletter Subscribe</h5></div>
  <div class="newsletter">Email Address
    <svg width="16" height="12" viewBox="0 0 16 12"><rect x="1" y="1" width="14" height="10" fill="none" stroke="#666" stroke-width="1.2"/><path d="M1 1l7 6 7-6" stroke="#666" stroke-width="1.2" fill="none"/></svg></div>
  <div class="follow">Follow us on</div>
  <div class="social"><i style="background:var(--navy)"></i><i style="background:var(--sky)"></i><i style="background:var(--navy)"></i><i style="background:var(--sky)"></i><i style="background:var(--navy)"></i><i style="background:var(--sky)"></i><i style="background:var(--navy)"></i></div>
</footer>

<div class="copyright abs">Copyright © 2017 Go Brightvale Solutions. All rights reserved.</div>

</div>
</body>
</html>
```